4 Header designs for dating sites

I need 4 difrant / unique headers for 2 adult dating sites, 1 non adult dating site and a cheat with an other wife/men site.

The headers need to be 840x140px
Colors are up to you. make it good looking.

The project price is for 4 unique headers.

the domains are:

Brovelkaan.nl (brovelkaan)
Grimbolderhuis.nl (grimbolderhouse)
Trevelinga.nl (trevelinga)
Mardouwke.nl (a dutch word for cheating)

Dating

use the domainnames

```html
<!DOCTYPE html>
<html lang="en">
<head>
<meta charset="utf-8">
<title>Dating site headers</title>
<link rel="stylesheet" href="https://fonts.googleapis.com/css2?family=Michroma&family=Poppins:wght@600;700&family=Rubik:wght@900&family=Varela+Round&display=swap">
<style>
  :root {
    --stage: #6f837c;
    --stage-dark: #40524c;
    --white: #ffffff;
    --ink: #1f1f24;
    --blue: #1e5fd0;
    --sky: #1aa0e0;
    --magenta: #b02e8a;
    --pink: #e0247f;
    --plum: #b0246e;
    --peach-1: #f7d6b6;
    --peach-2: #f4a574;
    --peach-3: #e77f6a;
    --skin-1: #d9a68a;
    --skin-2: #a7766a;
    --shirt: #9fb7d6;
  }
  * { box-sizing: border-box; margin: 0; padding: 0; }
  html, body { width: 1200px; height: 899px; overflow: hidden; }
  body {
    background: radial-gradient(ellipse at 30% 40%, #92a59e 0%, var(--stage) 55%, var(--stage-dark) 100%);
    position: relative;
  }
  .header {
    position: absolute;
    left: 120px;
    width: 960px;
    height: 160px;
    background: var(--white);
    box-shadow: 0 8px 18px rgba(0,0,0,.35);
    overflow: hidden;
  }
  .photo { position: absolute; top: 0; height: 100%; }

  /* Brovelkaan */
  .header--brovelkaan {
    top: 50px;
    background: linear-gradient(90deg, var(--peach-1) 30%, var(--peach-2) 70%, var(--peach-3) 100%);
  }
  .header--brovelkaan .photo {
    left: 0; width: 330px;
    background: linear-gradient(90deg, var(--skin-2), var(--skin-1) 70%, rgba(247,214,182,0));
  }
  .brovelkaan-tag {
    position: absolute; left: 385px; top: 22px;
    font-family: "Poppins", sans-serif; font-weight: 700; line-height: 1.05;
  }
  .brovelkaan-tag .line-1 { display: block; font-size: 24px; color: var(--ink); margin-left: 12px; }
  .brovelkaan-tag .line-2 { display: block; font-size: 30px; color: var(--blue); }
  .brovelkaan-name {
    position: absolute; left: 385px; top: 92px;
    font-family: "Michroma", sans-serif; font-size: 44px; letter-spacing: 4px;
    color: var(--magenta); text-transform: uppercase;
  }

  /* Grimbolderhouse */
  .header--grimbolderhouse { top: 260px; }
  .header--grimbolderhouse .photo {
    right: 0; width: 330px;
    background: linear-gradient(90deg, rgba(255,255,255,0), var(--skin-1) 35%, var(--shirt) 100%);
  }
  .grimbolderhouse-name {
    position: absolute; left: 40px; top: 22px;
    font-family: "Rubik", sans-serif; font-weight: 900; font-size: 50px;
    color: var(--blue); text-transform: uppercase; letter-spacing: 1px;
  }
  .grimbolderhouse-tag {
    position: absolute; left: 110px; top: 95px;
    font-family: "Poppins", sans-serif; font-weight: 600; font-size: 23px; color: var(--ink);
  }

  /* Trevelinga */
  .header--trevelinga { top: 470px; }
  .header--trevelinga .photo {
    right: 0; width: 250px;
    background: linear-gradient(90deg, rgba(255,255,255,0), var(--skin-1) 30%, var(--skin-2) 100%);
  }
  .trevelinga-mark {
    position: absolute; left: 40px; top: 30px;
    width: 100px; height: 100px; border-radius: 50%;
    background: var(--pink);
  }
  .trevelinga-name {
    position: absolute; left: 170px; top: 28px;
    font-family: "Varela Round", sans-serif; font-size: 84px; color: var(--plum);
    letter-spacing: -1px;
  }

  /* Mardouwke */
  .header--mardouwke { top: 680px; }
  .header--mardouwke .photo--left {
    left: 0; width: 200px;
    background: linear-gradient(90deg, #e9e3dc, #cfc6bd);
  }
  .header--mardouwke .photo--right {
    right: 0; width: 230px;
    background: linear-gradient(90deg, rgba(255,255,255,0), var(--skin-1) 35%, #c99c77 100%);
  }
  .mardouwke-tag {
    position: absolute; left: 240px; top: 18px;
    font-family: "Varela Round", sans-serif; font-weight: 400; line-height: 1;
  }
  .mardouwke-tag .line-1 { display: block; font-size: 58px; color: var(--sky); margin-left: 10px; }
  .mardouwke-tag .line-2 { display: block; font-size: 60px; color: var(--pink); margin-left: 180px; margin-top: 6px; }
</style>
</head>
<body>

<section class="header header--brovelkaan">
  <div class="photo" role="img" aria-label="Photo of a couple embracing on a beach at sunset"></div>
  <p class="brovelkaan-tag"><span class="line-1">Find your perfect</span><span class="line-2">sexual match!</span></p>
  <h1 class="brovelkaan-name">brovelkaan</h1>
</section>

<section class="header header--grimbolderhouse">
  <h1 class="grimbolderhouse-name">grimbolderhouse</h1>
  <p class="grimbolderhouse-tag">Find Your Sexually Compatible Match</p>
  <div class="photo" role="img" aria-label="Photo of a couple lying together in bed"></div>
</section>

<section class="header header--trevelinga">
  <div class="trevelinga-mark"></div>
  <h1 class="trevelinga-name">trevelinga</h1>
  <div class="photo" role="img" aria-label="Photo of a smiling woman with a man leaning in close"></div>
</section>

<section class="header header--mardouwke">
  <div class="photo photo--left" role="img" aria-label="Photo of a woman lying beside a laptop"></div>
  <p class="mardouwke-tag"><span class="line-1">a dutch word</span><span class="line-2">for cheating</span></p>
  <div class="photo photo--right" role="img" aria-label="Photo of a smiling couple cheek to cheek"></div>
</section>

</body>
</html>
```